New minimal and cool business card

We have a brand new logo - we would like to use the logo on blue on the front of the card
The tagline is The share and lend circle (tm)
We would like information on the back of the card for individual(s)

Our font is Lato
Our colors are indicated in the attached identity guide which uses the old logo - we are de-emphasizing orange

Please prepare the artwork to meet the specs on this site
http://us.prinvo.com/products/velora/business-cards.html

Front: Logo and tagline on dark blue

Back: On white
Join Today
http://zentaro.co/join

```html
<!DOCTYPE html>
<html lang="en">
<head>
<meta charset="utf-8">
<title>Zentaro Business Card</title>
<link rel="stylesheet" href="https://fonts.googleapis.com/css2?family=Lato:wght@300;400;700&display=swap">
<style>
  :root {
    --canvas-bg: #e9e7e3;
    --navy-top: #6e8398;
    --navy-mid: #3a5069;
    --navy-deep: #1b2c42;
    --brand-light: #e4e6e9;
    --brand-dark: #3d4a5a;
    --accent-orange: #f2a233;
    --ink-slate: #5d6d7f;
    --paper: #ffffff;
  }
  * { box-sizing: border-box; margin: 0; padding: 0; }
  html, body {
    width: 1200px; height: 900px; overflow: hidden;
    background: var(--canvas-bg);
    font-family: "Lato", Arial, sans-serif;
  }
  .canvas {
    position: relative; width: 1200px; height: 900px;
    display: flex; align-items: center; justify-content: center; gap: 40px;
  }
  .card {
    position: relative; width: 540px; height: 309px;
    box-shadow: 0 10px 28px rgba(0,0,0,0.18);
    overflow: hidden;
  }
  .card--front {
    background: linear-gradient(165deg, var(--navy-top) 0%, var(--navy-mid) 45%, var(--navy-deep) 100%);
  }
  .front-brand {
    position: absolute; left: 0; right: 0; top: 104px;
    text-align: center;
    font-weight: 400; font-size: 64px; letter-spacing: 1px;
    color: var(--brand-light);
  }
  .front-tagline {
    position: absolute; left: 0; right: 0; top: 200px;
    text-align: center;
    font-weight: 700; font-size: 19px;
    color: var(--accent-orange);
  }
  .front-tagline sup { font-size: 10px; }

  .card--back { background: var(--paper); }
  .back-brand {
    position: absolute; left: 44px; top: 168px;
    font-weight: 400; font-size: 34px; letter-spacing: 0.5px;
    color: var(--brand-dark);
  }
  .divider {
    position: absolute; left: 262px; top: 58px;
    width: 1.5px; height: 104px; background: var(--accent-orange);
  }
  .contact {
    position: absolute; left: 292px; top: 52px;
    color: var(--ink-slate); line-height: 1.2;
  }
  .contact-name { font-size: 17px; letter-spacing: 1.5px; font-weight: 400; }
  .contact-role { font-size: 14px; font-weight: 300; margin-bottom: 14px; }
  .contact-line { font-size: 14px; font-weight: 400; }
  .join {
    position: absolute; left: 292px; top: 196px;
    color: var(--ink-slate); font-size: 14px; line-height: 1.35;
  }
  .join-url { color: var(--brand-dark); }
</style>
</head>
<body>
  <main class="canvas">
    <section class="card card--front" aria-label="Card front">
      <div class="front-brand">zentaro</div>
      <p class="front-tagline">The share and lend circle<sup>™</sup></p>
    </section>

    <section class="card card--back" aria-label="Card back">
      <div class="back-brand">zentaro</div>
      <span class="divider"></span>
      <div class="contact">
        <p class="contact-name">JOHN SMITH</p>
        <p class="contact-role">Designation</p>
        <p class="contact-line">123-456-7890</p>
        <p class="contact-line">0984-654-321</p>
        <p class="contact-line">sample@mail.com</p>
      </div>
      <div class="join">
        <p>Join Today</p>
        <p class="join-url">http://zentaro.co/join</p>
      </div>
    </section>
  </main>
</body>
</html>
```